Postcard Design

I am a practicing Obstetrician and Gynecologist. I am working at a clinic called QRT Verano Care Network. I am looking for a design of a personal advertisement card that can be mailed, handed out, or sent an an electronic copy to the local newspaper to be placed as an ad. I previously worked for another clinic called JLW. They had an ad on my I liked very much, but I cannot use it. It is proprietary to them. I would like something like it. Copy attached. I want my foto and text. I have Printhaven Business Cards with QRT Verano and Stationary already. Access permitted. I would like to stay within that light blue - light green color scheme. I want the card to have me come across as competent and knowledgeable, but also as gentle, compassionate, benevolent, caring, knowledgeable, competent. Obviously, it has to appeal to women.

Target Market(s)

Public, patients, women

Industry/Entity Type

Electronic

Requirements
Nice to have
• A sophisticated, tasteful and inspiring maternity care image is very hard to find. I love the one on my business card. If it or something like it could be found and incorporated, that would be nice. I like a warm, soft, friendly font, Calibri light italic, Archer, Gotham. Describes nicely:Archer, the colorful slab serif. Sweet but not saccharine, earnest but not grave, Archer is designed to hit just the right notes of forthrightness, credibility, and charm.

```html
<!DOCTYPE html>
<html lang="en">
<head>
<meta charset="utf-8">
<title>Dr. Matthias Lindqvist – OB/GYN</title>
<link href="https://fonts.googleapis.com/css2?family=Jost:ital,wght@0,400;0,500;0,700;1,400;1,700&display=swap" rel="stylesheet">
<style>
  :root {
    --ink: #111111;
    --sky-top: #b9cfe0;
    --sky-warm: #f3dfa6;
    --sky-light: #eef1ee;
    --field: #a8cc55;
    --field-bright: #d9e23a;
    --panel: rgba(255, 255, 255, 0.88);
    --contact-wash: rgba(255, 255, 255, 0.5);
    --band: rgba(255, 255, 255, 0.82);
    --coat: #f4f4f2;
    --skin: #e6c3b2;
  }
  html, body {
    margin: 0;
    padding: 0;
    width: 1200px;
    height: 926px;
    overflow: hidden;
  }
  body {
    font-family: "Jost", "Century Gothic", sans-serif;
    color: var(--ink);
  }
  .card {
    position: relative;
    width: 1200px;
    height: 926px;
    overflow: hidden;
  }
  .backdrop {
    position: absolute;
    inset: 0;
    background: linear-gradient(180deg, var(--sky-top) 0%, var(--sky-warm) 22%, var(--sky-light) 45%, #e3ecd8 62%, var(--field) 82%, var(--field-bright) 100%);
  }
  .portrait {
    position: absolute;
    left: 0;
    top: 24px;
    width: 500px;
    height: 812px;
    border-radius: 220px 240px 0 0;
    background:
      radial-gradient(ellipse 42% 30% at 52% 28%, var(--skin) 0%, rgba(230, 195, 178, 0.6) 60%, rgba(244, 244, 242, 0) 100%),
      linear-gradient(180deg, #9c9c9c 0%, #d8c2b5 18%, var(--coat) 50%, var(--coat) 100%);
  }
  .info-panel {
    position: absolute;
    left: 487px;
    top: 50px;
    width: 661px;
    height: 718px;
    box-sizing: border-box;
    padding: 36px 24px 0 27px;
    background: var(--panel);
  }
  .doctor-name {
    margin: 0;
    text-align: center;
    white-space: nowrap;
    font-weight: 700;
    font-size: 33px;
    line-height: 1.2;
    letter-spacing: -0.3px;
  }
  .doctor-name .nickname { font-style: italic; }
  .credentials {
    margin: 2px 0 0;
    text-align: center;
    font-size: 32px;
    line-height: 1.1;
  }
  .specialty {
    margin: 6px 0 0;
    text-align: center;
    font-size: 21px;
    letter-spacing: 0.3px;
  }
  .body-copy {
    font-size: 19.5px;
    line-height: 28.6px;
    text-align: justify;
  }
  .intro { margin: 22px 0 0; }
  .education { margin: 28px 0 0; }
  .education p { margin: 0; text-align: left; }
  .focus { margin: 28px 0 0; }
  strong { font-weight: 700; }
  .contact {
    position: absolute;
    left: 0;
    right: 0;
    top: 563px;
    bottom: 0;
    box-sizing: border-box;
    padding: 16px 24px 0 27px;
    display: flex;
    font-size: 19.5px;
    line-height: 28.6px;
    background: var(--contact-wash);
  }
  .contact p { margin: 0; }
  .contact .address { width: 297px; }
  .contact .fax { margin-top: 28.6px; }
  .plans-band {
    position: absolute;
    left: 0;
    top: 836px;
    width: 1200px;
    height: 78px;
    box-sizing: border-box;
    padding: 12px 38px 0;
    background: var(--band);
    font-style: italic;
    font-size: 17.6px;
    line-height: 26.5px;
    letter-spacing: 0.1px;
  }
  .plans-band p { margin: 0; }
</style>
</head>
<body>
  <main class="card">
    <div class="backdrop" role="img" aria-label="Soft photographic backdrop of a sunlit sky over a green meadow"></div>
    <div class="portrait" role="img" aria-label="Portrait photo of the doctor, smiling, wearing a white coat"></div>

    <section class="info-panel">
      <h1 class="doctor-name">MATTHIAS R. <span class="nickname">(“ MATT ”)</span> LINDQVIST</h1>
      <p class="credentials">MD, FACOG</p>
      <p class="specialty">BOARD CERTIFIED OBSTETRICIAN &amp; GYNECOLOGIST</p>

      <p class="body-copy intro"><strong>Dr. Lindqvist</strong> is a Board Certified OB/GYN and was in private practice in Atlanta, Georgia for twenty-five years. He recently was the in-house hospitalist Obstetrics and Gynecology at the Harbor Point Memorial Hospital.</p>

      <div class="body-copy education">
        <p><strong>Education:</strong></p>
        <p>University of Elbhaven School of Medicine, Germany</p>
        <p><strong>Residency and Internship:</strong></p>
        <p>Eastbrook University School of Medicine, New York</p>
        <p><strong>Residency:</strong> University of Riverbend School of Medicine, Kentucky</p>
      </div>

      <p class="body-copy focus">Dr. Lindqvist specializes in preventive medicine and women’s wellness and weight management</p>

      <div class="contact">
        <div class="address">
          <p><strong>Accepting New Patients at</strong></p>
          <p>QRT Verano Care Network</p>
          <p>214-B Calle Marisol</p>
          <p>Port Calder, ST 40213</p>
        </div>
        <div class="phone">
          <p>Please call for an appointment at</p>
          <p><strong>555-014-2780</strong></p>
          <p class="fax">Fax: 555-014-2791</p>
        </div>
      </div>
    </section>

    <footer class="plans-band">
      <p>CREDENTIALED PROVIDER WITH MERIDIAN GLOBAL, HARBOR CROSS / HARBOR SHIELD, ALDEN’S SELECTCARE, STATECARE PLUS, SENIORCARE,</p>
      <p>KLP, LINKCARE, WELLSTAY, TENDCARE, TRICREST.&nbsp; REFERRAL REQUIRED WITH SOME PLANS.</p>
    </footer>
  </main>
</body>
</html>
```